Veltrona Web Presence

I need a word press site for my company that houses diverse services, and am looking to profile these areas: Design and Delivery of Social Innovation Initiatives, Innovative Pubic Engagement, The Turquoise Economy, Youth Entrepreneurship, and The Science of Change.

I would also like to profile my recent projects. A blog, video and photos are also important features.

Industry/Entity Type

It Company

Requirements
Must have
• I would like to have an overview of what the company does as a Think, Feel and Do Company, along with sections for specific services and recent project profiles.

I would like a section for a blog

I would like a section for photos and video.

I would like the look and feel of the website to reflect the following:

Marisol has spent 30 years leading expeditions into the future. Marisol has a special interest in exploring the changing business, social and cultural landscapes and frontiers, uncovering uncharted territory and unleashing hidden potential – within the person, family, organization, community, business or marketplace. Marisol thrives on experimentation that has led to blended eastern and western methodologies and technologies that help people and organizations deal with the chronic and tough issues in research-based, intelligent and inspiring ways.

Specialties:Breaking down the walls between disciplines such as environmental, social, and economic approaches to create ideologies and methodologies that weave them all to change the way we live. This ideology and methodology applies to all areas: business development, business identity, strategy for all organizations - public, private and NGO.This starts at the individual level.Marisol is also an energy healer specializing in belief reconstruction leading to fulfilling lives.

```html
<!DOCTYPE html>
<html lang="en">
<head>
<meta charset="utf-8">
<title>Veltrona</title>
<link href="https://fonts.googleapis.com/css2?family=Open+Sans:wght@400;600&family=PT+Sans+Narrow:wght@400;700&family=Raleway:wght@400&display=swap" rel="stylesheet">
<style>
:root{
  --blue:#1f74bd;
  --blue-dark:#135a9c;
  --nav-top:#4d9ad8;
  --nav-bottom:#2b78bf;
  --nav-active:#4a4a4a;
  --accent:#2a7fc4;
  --ink:#444;
  --muted:#555;
  --red:#b51f24;
  --footer:#3d3d3d;
  --orange:#f7a21b;
  --white:#fff;
}
*{box-sizing:border-box;margin:0;padding:0}
html,body{width:960px;height:1200px;overflow:hidden}
body{font-family:"Open Sans",sans-serif;color:var(--ink);background:linear-gradient(#1d6fb8 0,#2a7ac1 600px,#4f98d2 1068px);position:relative}
.abs{position:absolute}
.header{left:0;top:0;width:960px;height:83px;background:linear-gradient(#fff,#eef0f2)}
.logo{left:98px;top:20px;display:flex;align-items:center;gap:8px}
.logo-dot{width:22px;height:22px;border-radius:50%;background:var(--accent)}
.logo-name{font-family:"Raleway",sans-serif;font-size:40px;color:var(--accent);line-height:1}
.contact{top:30px;display:flex;align-items:center;gap:8px;font-size:11px;color:#555}
.contact svg{display:block}
.phone{font-size:15px;color:var(--red);font-weight:600}
.nav{left:0;top:83px;width:960px;height:45px;background:linear-gradient(var(--nav-top),var(--nav-bottom))}
.nav ul{list-style:none;position:absolute;left:89px;top:0;display:flex;height:45px}
.nav li{font-family:"PT Sans Narrow",sans-serif;font-weight:700;font-size:15px;color:#fff;padding:0 19px;line-height:45px;border-right:1px solid rgba(255,255,255,.35);text-transform:uppercase}
.nav li.active{background:var(--nav-active);padding:0 27px}
.nav li:last-child{border:none}
.search{left:754px;top:97px;width:114px;height:19px;border-radius:10px;background:#fff;overflow:hidden;display:flex;font-size:9px;color:#555;align-items:center;padding-left:10px}
.search span{flex:1}
.search i{width:22px;height:19px;background:var(--orange);display:flex;align-items:center;justify-content:center}
.slider{left:91px;top:152px;width:779px;height:293px;background:#f4f4f4;box-shadow:0 4px 8px rgba(0,0,0,.25)}
.slide-img{left:102px;top:162px;width:758px;height:272px;background:radial-gradient(ellipse at 65% 45%,#3a4448,#1a1d1f 60%,#000 100%)}
.slide-copy{left:121px;top:222px;width:216px;color:#fff}
.slide-copy h2{font-family:"Open Sans",sans-serif;font-weight:400;font-size:13px;letter-spacing:.4px;white-space:nowrap;line-height:16px;margin-bottom:14px}
.slide-copy p{font-size:10.2px;line-height:14.4px;text-align:justify}
.more-btn{left:252px;top:349px;width:84px;height:26px;border-radius:4px;background:linear-gradient(#ffd23a,#f59d10);color:#fff;font-family:"PT Sans Narrow",sans-serif;font-weight:700;font-size:13px;text-align:center;line-height:26px}
.arrow{top:290px;width:24px;height:26px;background:#555;color:#fff;font-size:10px;display:flex;align-items:center;justify-content:center}
.arrow.l{left:91px;border-radius:13px 0 0 13px}
.arrow.r{left:846px;border-radius:0 13px 13px 0}
.card{top:465px;width:189px;height:205px;background:#fff}
.card h3{font-weight:400;font-size:13px;color:#1f5d8f;padding:10px 0 0 0;text-align:center;white-space:nowrap}
.card .thumb{position:absolute;left:8px;top:32px;width:173px;height:86px;border:2px solid #ccc}
.card p{position:absolute;left:6px;top:128px;width:177px;font-size:8.6px;line-height:12.8px;color:var(--muted);text-align:justify}
.card .rm{position:absolute;right:12px;top:174px;width:84px;height:20px;border-radius:10px;background:linear-gradient(#7ec0f2,#3c91dc);color:#fff;font-size:9.5px;font-weight:600;text-align:center;line-height:20px}
.panel{left:88px;top:697px;width:785px;height:371px;background:linear-gradient(#fff,#efefef)}
.sec-title{font-family:"PT Sans Narrow",sans-serif;font-weight:700;font-size:20px;color:#333}
.sec-title b{color:var(--accent);font-weight:700}
.rule{height:0;border-top:1px dotted #999}
.blog-item{left:112px;width:460px}
.blog-item .thumb{position:absolute;left:0;top:0;width:110px;height:67px;border:2px solid #ddd;box-shadow:0 1px 2px rgba(0,0,0,.2)}
.blog-item h4{position:absolute;left:120px;top:0;font-weight:400;font-size:11.5px;color:#333}
.blog-item p{position:absolute;left:120px;top:16px;width:330px;font-size:9.4px;line-height:14.5px;color:var(--muted);text-align:justify}
.blog-item .more{position:absolute;font-size:9.6px;color:var(--red);white-space:nowrap}
.dots{display:flex;gap:8px}
.dots i{width:10px;height:10px;border-radius:50%;background:#e8601c;display:block}
.media{width:127px;height:94px;border:3px solid #eee;box-shadow:0 3px 4px rgba(0,0,0,.2)}
.media .cap{position:absolute;left:0;bottom:0;width:100%;height:23px;background:rgba(60,60,60,.6);color:#fff;font-family:"PT Sans Narrow",sans-serif;font-size:13px;line-height:23px;padding-left:5px}
.media .play{position:absolute;left:50%;top:30%;width:18px;height:18px;margin-left:-9px;border-radius:50%;background:rgba(255,255,255,.8)}
.footer{left:0;top:1068px;width:960px;height:132px;background:var(--footer)}
.sub-title{left:104px;top:1082px;font-family:"PT Sans Narrow",sans-serif;font-weight:700;font-size:17px;color:#fff}
.email{left:104px;top:1112px;width:206px;height:25px;background:#fff;border:1px solid #ccc;font-size:8.5px;font-style:italic;color:#888;padding:7px 12px}
.sub-btn{left:227px;top:1146px;width:83px;height:25px;background:var(--red);color:#fff;font-family:"PT Sans Narrow",sans-serif;font-weight:700;font-size:13px;text-align:center;line-height:25px}
.social{left:696px;top:1093px;display:flex;gap:9.5px}
.social i{width:21px;height:21px;display:block;background:#6f7f8f;border:1px solid #888}
.copy{left:700px;top:1129px;width:173px;text-align:right;font-size:8.5px;color:#ddd}
</style>
</head>
<body>
<header class="header abs">
  <div class="logo abs"><span class="logo-dot"></span><span class="logo-name">Veltrona</span></div>
  <div class="contact abs" style="left:537px">
    <svg width="25" height="17" viewBox="0 0 25 17"><rect x=".5" y=".5" width="24" height="16" fill="#f4f4f4" stroke="#aab"/><path d="M1 1l11.5 9L24 1" fill="none" stroke="#aab"/></svg>
    <span>info@veltrona.com</span>
  </div>
  <div class="contact abs" style="left:710px;top:28px">
    <svg width="22" height="22" viewBox="0 0 22 22"><rect width="22" height="22" rx="4" fill="#2a6fb5"/><path d="M7 5c1 0 2 2 2 3s-1 1-1 2 2 3 3 4 1-1 2-1 3 1 3 2-1 2-2 2C10 17 5 12 5 7c0-1 1-2 2-2z" fill="#fff"/></svg>
    <span class="phone">+61 2 5550 1842</span>
  </div>
</header>

<nav class="nav abs">
  <ul>
    <li class="active">Home</li><li>About Us</li><li>Services</li><li>Blog</li><li>Testmonials</li><li>Contact Us</li>
  </ul>
</nav>
<div class="search abs"><span>Search</span><i><svg width="11" height="11" viewBox="0 0 11 11"><circle cx="4.5" cy="4.5" r="3.3" fill="none" stroke="#fff" stroke-width="1.4"/><path d="M7 7l3 3" stroke="#fff" stroke-width="1.6"/></svg></i></div>

<div class="slider abs"></div>
<div class="slide-img abs" role="img" aria-label="Chalkboard with the word innovation drawn inside a thought bubble"></div>
<div class="slide-copy abs">
  <h2>SOCIAL INNOVATION INITIATIVES</h2>
  <p>Sed ut perspiciatis unde omnis iste natus error sit voluptatem accusantium doloremque laudantium, totam rem aperiam, eaque ipsa quae ab illo inventore veritatis et quasi architecto beatae vitae dicta sunt explicabo. Nemo enim ipsam</p>
</div>
<div class="more-btn abs">MORE</div>
<div class="arrow l abs">«</div>
<div class="arrow r abs">»</div>

<section class="card abs" style="left:89px">
  <h3>Social Innovation Initiatives</h3>
  <div class="thumb" role="img" aria-label="Row of light bulbs with one glowing" style="background:linear-gradient(#1a2c44,#3a6fa8)"></div>
  <p>Sed ut perspiciatis unde omnis iste natus error voluptatem accusantium doloremque otam rem aperiam, eaque ipsa quae ab illo inventore veritatis.</p>
  <div class="rm">Read More &gt;&gt;</div>
</section>
<section class="card abs" style="left:287px">
  <h3>Innovative Pubic Engagement</h3>
  <div class="thumb" role="img" aria-label="Protest placards held up in a crowd" style="background:linear-gradient(90deg,#c9c4bd,#e6e2dc,#b9aea6)"></div>
  <p>Sed ut perspiciatis unde omnis iste natus error voluptatem accusantium doloremque otam rem aperiam, eaque ipsa quae ab illo inventore veritatis.</p>
  <div class="rm">Read More &gt;&gt;</div>
</section>
<section class="card abs" style="left:486px">
  <h3>Youth Entrepreneurship</h3>
  <div class="thumb" role="img" aria-label="Light bulb containing a globe" style="background:radial-gradient(circle at 70% 40%,#fff,#c8d4e0 60%,#9fb1c4)"></div>
  <p>Sed ut perspiciatis unde omnis iste natus error voluptatem accusantium doloremque otam rem aperiam, eaque ipsa quae ab illo inventore veritatis.</p>
  <div class="rm">Read More &gt;&gt;</div>
</section>
<section class="card abs" style="left:683px">
  <h3>Private Healing Sessions</h3>
  <div class="thumb" role="img" aria-label="Figure dissolving into leaves in a misty landscape" style="background:linear-gradient(#8a8f8f,#5f6a5a 70%,#4a5a3c)"></div>
  <p>Sed ut perspiciatis unde omnis iste natus error voluptatem accusantium doloremque otam rem aperiam, eaque ipsa quae ab illo inventore veritatis.</p>
  <div class="rm">Read More &gt;&gt;</div>
</section>

<main class="panel abs"></main>

<h2 class="sec-title abs" style="left:106px;top:708px">Latest <b>Blog</b></h2>
<div class="rule abs" style="left:106px;top:736px;width:458px"></div>

<article class="blog-item abs" style="top:762px">
  <div class="thumb" role="img" aria-label="Hand writing notes on paper" style="background:linear-gradient(135deg,#c9a88e,#f0eeea 50%,#dfe3e6)"></div>
  <h4>Sed ut Perspiciatis Unde Omni</h4>
  <p>voluptatem accusantium doloremque laudantium, totam rem aperiam, eaque ipsa quae ab illo inventore veritatisvoluptatem accusantium doloremque laudantium, totam rem aperiamveritatisvoluptatem accusantium doloremque laudantium</p>
  <span class="more" style="left:418px;top:70px">MORE &gt;&gt;</span>
</article>
<article class="blog-item abs" style="top:859px">
  <div class="thumb" role="img" aria-label="Crowd of colourful figures under a light bulb" style="background:linear-gradient(#fbf7e8 45%,#d96a4a 75%,#3e8d6a)"></div>
  <h4>Sed ut Perspiciatis Unde Omni</h4>
  <p>voluptatem accusantium doloremque laudantium, totam rem aperiam, eaque ipsa quae ab illo inventore veritatisvoluptatem accusantium doloremque laudantium, totam rem aperiamveritatisvoluptatem accusantium doloremque laudantium</p>
  <span class="more" style="left:402px;top:67px">MORE &gt;&gt;</span>
</article>
<article class="blog-item abs" style="top:956px">
  <div class="thumb" role="img" aria-label="Two friends wearing sunglasses" style="background:linear-gradient(90deg,#a26a3c,#d9a27a 50%,#8a5a34)"></div>
  <h4>Sed ut Perspiciatis Unde Omni</h4>
  <p>voluptatem accusantium doloremque laudantium, totam rem aperiam, eaque ipsa quae ab illo inventore veritatisvoluptatem accusantium doloremque laudantium, totam rem aperiamveritatisvoluptatem accusantium doloremque laudantium</p>
  <span class="more" style="left:403px;top:65px">MORE &gt;&gt;</span>
</article>

<h2 class="sec-title abs" style="left:595px;top:708px">Our <b>Photos</b></h2>
<div class="dots abs" style="left:829px;top:718px"><i></i><i></i></div>
<div class="rule abs" style="left:595px;top:736px;width:268px"></div>
<div class="media abs" style="left:592px;top:748px;background:linear-gradient(#7a2a24,#2a2a30 60%,#c9c2b8)" role="img" aria-label="Businessman seated on a bench"><span class="cap">Loreum Ipsum</span></div>
<div class="media abs" style="left:734px;top:748px;background:linear-gradient(#5a88c2,#cfe0f0 55%,#e8eef3)" role="img" aria-label="Woman with outstretched arms under a blue sky"><span class="cap">Dollar Amet</span></div>

<h2 class="sec-title abs" style="left:595px;top:869px">Our <b>Videos</b></h2>
<div class="dots abs" style="left:829px;top:879px"><i></i><i></i></div>
<div class="rule abs" style="left:595px;top:897px;width:268px"></div>
<div class="media abs" style="left:592px;top:909px;background:radial-gradient(circle at 50% 55%,#f6c47a,#b05a1c 45%,#2a1408)" role="img" aria-label="Hands cupping a glowing light bulb"><span class="play"></span><span class="cap">Loreum Ipsum</span></div>
<div class="media abs" style="left:736px;top:909px;background:linear-gradient(160deg,#6f8fb5,#2f7a4a 50%,#1f5a38)" role="img" aria-label="Green road sign reading innovation exchange"><span class="play"></span><span class="cap">Loreum Ipsum</span></div>

<footer class="footer abs"></footer>
<h3 class="sub-title abs">Subscribe to Veltrona</h3>
<div class="email abs">Your Email Id</div>
<div class="sub-btn abs">Subscribe</div>
<div class="social abs" aria-label="Social links"><i></i><i></i><i></i><i></i><i></i><i></i></div>
<p class="copy abs">© 2013 Veltrona, All rights reserved</p>
</body>
</html>
```